Whale Watching Voucher(ticket) Layout

Tidalroam.com.au would like a new design for their existing vouchers (tickets) being issued when a customer completes a purchase.
These vouchers are to be issued from within Salesforce CRM using Conga Composer (don't worry about that, we'll handle that) but that does mean that the voucher template needs to be designed and provided in Microsoft Word. The voucher will be sent via an email and we require a HTML email design also.
The following fields need to be included on the email/Voucher:
BOOKING CONFIRMATION NUMBER (e&v)
First Name (e&v)
Tour Name (e&v)
Tour Operator Name (e&v)
Telephone Contact (e&v)
Departure Date (e&v)
Party Name (e&v)
Adults Tickets (v)
Concession Tickets (v)
Child Tickets (v)
Infant Tickets (v)
Pickup Location (v)
Pickup Time (v)
Boarding Place (v)
Boarding Time (v)
Departure Time (v)
Return Time (v)
Terms and conditions (e&v) - this is quite a long description
What to Bring (v) - this is quite a long description
What to do if the Pick-up is more than 10 mins late (v) - this is a long description
What to do if you're late (v) - this is quite a long description
Booking Terms and Conditions
{!Opportunity.Tour_Terms_and_Conditions_PG1__c}
FREECALL 1800 437 962 (Australia)
International +61 7 5926 8174
Skype journeymoss
(e&v indicate fields to be included on the Email and the Voucher)
(v indicate fields to be included on the Voucher only)
Updates
Project Deadline Extended
Reason: I realised the original Deadline didn't take weekends into account so have extended it to the end of this week. The Whale season is well underway so need to have it completed by Friday. Thanks all for your efforts.
I uploaded the current (text based) samples of the email & voucher that we are hoping you are going to be able to redesign for us.
Sorry for lack of feedback, I got caught up on another project. We are reviewing the designs tomorrow and will get back to you all.
Target Market(s)
Mid market Australian and International Tourists
Industry/Entity Type
Purchase
Requirements
Must have
- Consistency with existing Tidalroam.com.au & coralpath.com.au branding.
The Voucher should be designed to be printed out on a single A4 sheet.
Nice to have
- It would be good to have a paragraph/section referencing the coralpath.com.au logo and website on the email (not the voucher).
Any recommendation for additional information/fields that should/could be included not listed above will be gratefully received.
Happy for you to reword the labels to make them more friendly.

```html
<!DOCTYPE html>
<html lang="en">
<head>
<meta charset="utf-8">
<title>Tidalroam Booking Voucher</title>
<link href="https://fonts.googleapis.com/css2?family=Carlito:wght@400;700&family=Open+Sans:wght@400;700&display=swap" rel="stylesheet">
<style>
  :root {
    --teal: #1aa396;
    --teal-dark: #13897e;
    --teal-light: #d4efec;
    --card-head: #bfe6e2;
    --sand: #ece4d1;
    --ink: #1c1c1c;
    --white: #ffffff;
  }
  * { margin: 0; padding: 0; box-sizing: border-box; }
  html, body { width: 848px; height: 1200px; overflow: hidden; background: var(--white); }
  .voucher {
    position: relative; width: 848px; height: 1200px; overflow: hidden;
    background: var(--white); color: var(--ink);
    font-family: "Carlito", "Calibri", sans-serif;
  }
  .hero-band { position: absolute; left: 0; top: 72px; width: 848px; height: 504px; background: var(--teal-light); }
  .brand { position: absolute; left: 52px; top: 34px; display: flex; align-items: center; gap: 14px; }
  .brand-dot { width: 74px; height: 74px; border-radius: 50%; background: var(--teal); }
  .brand-name { font-family: "Open Sans", sans-serif; font-size: 27px; font-weight: 400; color: var(--teal); }
  .boat-art { position: absolute; left: 484px; top: 18px; width: 248px; height: 112px;
    background: linear-gradient(180deg, #bfe6e2 0%, #1aa396 100%); border-radius: 18px 40px 30px 8px; }
  .booking-card {
    position: absolute; left: 138px; top: 130px; width: 588px; height: 422px;
    background: var(--white); border: 3px solid var(--teal); border-radius: 22px; overflow: hidden;
  }
  .card-head { height: 58px; background: var(--card-head); display: flex; align-items: center; justify-content: center; }
  .card-title { font-family: "Open Sans", sans-serif; font-weight: 700; font-size: 17px; }
  .fields { position: absolute; left: 75px; top: 96px; width: 460px; font-family: "Open Sans", sans-serif; font-size: 13px; line-height: 17.3px; }
  .fields + .fields { top: 287px; }
  .field { display: flex; }
  .field dt { width: 277px; font-weight: 700; }
  .field dd { font-weight: 400; }
  .bring-band { position: absolute; left: 0; top: 584px; width: 848px; height: 60px; background: var(--sand); padding: 14px 52px 0; font-size: 16px; line-height: 20px; }
  .heading { font-weight: 700; }
  .terms { position: absolute; left: 52px; top: 660px; width: 760px; font-size: 16px; line-height: 20px; }
  .terms p { margin-bottom: 20px; }
  .terms .lead { margin-bottom: 19px; }
  .footer-wave { position: absolute; left: 0; bottom: 0; width: 848px; height: 140px; }
  .tail-art { position: absolute; left: 668px; top: 1016px; width: 120px; height: 96px;
    background: var(--teal); border-radius: 50% 50% 10px 60%; }
  .contact-bar { position: absolute; left: 0; bottom: 20px; width: 848px; display: flex; justify-content: space-between; padding: 0 34px;
    font-family: "Open Sans", sans-serif; font-weight: 700; font-size: 16.5px; color: var(--white); }
</style>
</head>
<body>
<main class="voucher">
  <div class="hero-band"></div>

  <div class="brand">
    <span class="brand-dot"></span>
    <span class="brand-name">TIDALROAM</span>
  </div>
  <div class="boat-art" role="img" aria-label="Illustration of a whale watching cruise boat"></div>

  <section class="booking-card">
    <header class="card-head"><h1 class="card-title">BOOKING CONFIRMATION NUMBER (e&amp;v)</h1></header>
    <dl class="fields">
      <div class="field"><dt>First Name (e&amp;v)</dt><dd>First Name (e&amp;v)</dd></div>
      <div class="field"><dt>Tour Name (e&amp;v)</dt><dd>Tour Name (e&amp;v)</dd></div>
      <div class="field"><dt>Tour Operator Name (e&amp;v)</dt><dd>Tour Operator Name (e&amp;v)</dd></div>
      <div class="field"><dt>Telephone Contact (e&amp;v)</dt><dd>Telephone Contact (e&amp;v)</dd></div>
      <div class="field"><dt>Departure Date (e&amp;v)</dt><dd>Departure Date (e&amp;v)</dd></div>
      <div class="field"><dt>Party Name (e&amp;v)</dt><dd>Party Name (e&amp;v)</dd></div>
      <div class="field"><dt>Adults Tickets (v)</dt><dd>Adults Tickets (v)</dd></div>
      <div class="field"><dt>Concession Tickets (v)</dt><dd>Concession Tickets (v)</dd></div>
      <div class="field"><dt>Child Tickets (v)</dt><dd>Child Tickets (v)</dd></div>
      <div class="field"><dt>Infant Tickets (v)</dt><dd>Infant Tickets (v)</dd></div>
    </dl>
    <dl class="fields">
      <div class="field"><dt>Pickup Location (v)</dt><dd>Pickup Location (v)</dd></div>
      <div class="field"><dt>Pickup Time (v)</dt><dd>Pickup Time (v)</dd></div>
      <div class="field"><dt>Boarding Place (v)</dt><dd>Boarding Place (v)</dd></div>
      <div class="field"><dt>Boarding Time (v)</dt><dd>Boarding Time (v)</dd></div>
      <div class="field"><dt>Departure Time (v)</dt><dd>Departure Time (v)</dd></div>
      <div class="field"><dt>Return Time (v)</dt><dd>Return Time (v)</dd></div>
    </dl>
  </section>

  <section class="bring-band">
    <h2 class="heading">What to Bring:</h2>
    <p>Hat, swimmers, walking shoes, towel, sunscreen, camera, water bottle and a smile!</p>
  </section>

  <section class="terms">
    <h2 class="heading">Terms and Conditions:</h2>
    <p class="lead">Tidalroam are agent for Sandbar Experience Tours</p>
    <p>Cancellations within 48 hours of tour departure and/or failure to board on tour date will incur 100% non-refundable cancellation fee.<br>
    Transfers to another tour date are not allowed within 24 hours of departure unless at management discretion.
    When transfers are granted to alternative tour date payment for the tour is to be made by the customer at the time of transfer.<br>
    Sandbar Experience Tours reserve the right to operate substitute vehicle, accommodation, food and drinks, and amend tour itinerary without prior notification.</p>
    <p>Minimum numbers apply.</p>
    <p>Directors, managers and staff shall not be responsible or liable for death or/or injury to any person, or loss of/damage to any property due to persons’ negligence.</p>
    <p>This is an off road 4WD tour and track conditions can be rough at various times of the year on Fraser Island. We recommend you consult your doctor if you have a pre-existing medical condition (back pain, pregnancy, motion sickness, etc) that may be affected by this.</p>
  </section>

  <svg class="footer-wave" viewBox="0 0 848 140" preserveAspectRatio="none" aria-hidden="true">
    <path d="M0 40 C120 10 240 60 380 40 C520 20 640 55 848 30 L848 140 L0 140 Z" fill="#bfe6e2"/>
    <path d="M0 62 C140 36 260 78 420 58 C560 40 700 72 848 50 L848 140 L0 140 Z" fill="#1aa396"/>
  </svg>
  <div class="tail-art" role="img" aria-label="Illustration of a whale tail rising from the water"></div>

  <footer class="contact-bar">
    <span>FREE CALL:1800 437 962 (Australia)</span>
    <span>International:+61 7 5926 8174</span>
    <span>Skype:journeymoss</span>
  </footer>
</main>
</body>
</html>
```